Product label for herbal salves, lotions, soaps and tinctures

We need a very simple, clean and organic looking label that can be used for an ointment jar, a lotion bottle and a dropper bottle.
We have an existing logo (see attached). We like the colors white, olive green, gold and black. It needs to include product name as dominant and logo. It also needs to include an ingredient list, and usage statement. Include weight of product, distributed by, made in the USA, and QRB statement.
Example of what needs to be present:
Logo
Name: Sunward Blend Tonic
Used for: For Muscle Aches, Arthritis, Tendonitis, Headaches
To Use: For muscle aches, arthritis and tendonitis, massage into affected area. For tension headache apply to neck, temples and forehead.
Store in a cool and dry place, away from direct heat and sunlight.
Weight of product: 1.75
DIST. BY: Brightmoor Herbal
Made in the USA
This product is not intended to diagnose, treat, cure
or prevent any disease. Not regulated
by the QRB. Please consult your health care practitioner
before using product. Discontinue use if any adverse reaction occurs.
Ingredient list:
Wildcrafted Ingredients:
Ashwagandha Root, Peppermint Leaf, Hops Flowers, St. John’s Wort Herb, Arnica Flowers, Green Tea Leaf, Alfalfa Leaf, Dandelion Root, Burdock Root, Chickweed Herb, Chaparral Leaf, Yarrow Flowers, Boneset Herb, Moringa Leaf, Meadowsweet Herb, Nettle Leaf
Organic Ingredients:
Olive Oil, Aloe Leaf, Sweet Birch Bark, Helichrysum Flowers, Holy Basil Leaf, Borage Herb, Ginger Root, Angelica Root, White Willow Bark, Mustard Seed, Beeswax, Vitamin E, Essential Oils
Dimensions of Jar:
Circumference: 7 in.
Height: 1 in.

```html
<!DOCTYPE html>
<html lang="en">
<head>
<meta charset="utf-8">
<title>Sunward Blend Tonic – Jar Label</title>
<link href="https://fonts.googleapis.com/css2?family=Marcellus&family=Barlow:ital,wght@0,400;0,500;0,600;1,600&display=swap" rel="stylesheet">
<style>
  :root{
    --paper:#ffffff;
    --ink:#1c1c1c;
    --olive:#6f7132;
    --olive-soft:#e6e6dc;
    --gold-dark:#8e5a26;
    --gold-mid:#c99a4a;
    --gold-light:#f3e08a;
  }
  *{box-sizing:border-box;margin:0;padding:0}
  html,body{width:1200px;height:1157px;overflow:hidden;background:var(--paper)}
  body{position:relative;font-family:"Barlow",sans-serif;color:var(--ink)}
  .label{position:absolute;left:28px;top:500px;width:1144px;height:158px;background:var(--paper)}
  .gold-rule{position:absolute;left:0;right:0;height:6px;
    background:linear-gradient(90deg,var(--gold-dark) 0%,var(--gold-mid) 25%,var(--gold-light) 50%,var(--gold-mid) 75%,var(--gold-dark) 100%)}
  .gold-rule.top{top:0}
  .gold-rule.bottom{bottom:0}

  .ingredients{position:absolute;left:19px;top:10px;width:313px;font-size:10.4px;line-height:11.6px;text-align:justify}
  .ingredients h3{font-weight:600;font-size:10.4px;letter-spacing:.1px}
  .ingredients h4{font-weight:600;font-style:italic;color:var(--olive);font-size:10.4px}

  .center{position:absolute;left:408px;top:16px;width:300px;text-align:center}
  .product-name{font-family:"Marcellus",serif;font-size:23px;letter-spacing:.8px;text-transform:uppercase;font-weight:400;white-space:nowrap}
  .brand-row{display:flex;align-items:center;justify-content:center;margin-top:14px;gap:14px}
  .brand-name{font-family:"Barlow",sans-serif;font-weight:600;font-size:17px;color:var(--olive);line-height:1.05;text-align:left}
  .uses{border-left:1px solid var(--ink);padding-left:8px;font-size:10.6px;line-height:13.5px;text-align:left}

  .directions{position:absolute;left:752px;top:14px;width:180px;font-size:10.2px;line-height:11.6px;text-align:justify}
  .directions em{font-style:italic;font-weight:600;color:var(--olive)}
  .directions p+p{margin-top:11px}
  .weight{position:absolute;left:836px;top:130px;font-size:10.4px;font-weight:600}

  .notice{position:absolute;left:956px;top:12px;width:154px;font-size:9.2px;line-height:9.4px;text-align:justify}
  .made{position:absolute;left:956px;top:84px;width:154px;text-align:center;font-size:10.4px;font-style:italic;font-weight:600;color:var(--olive)}
  .dist{position:absolute;left:940px;top:114px;width:170px;text-align:right;font-size:10.4px;font-weight:600}
  .web{position:absolute;left:940px;top:130px;width:170px;text-align:right;font-size:10.4px}
</style>
</head>
<body>
  <section class="label" aria-label="Sunward Blend Tonic jar label">
    <div class="gold-rule top"></div>

    <div class="ingredients">
      <h3>INGREDIENT LIST:</h3>
      <h4>Wildcrafted Ingredients:</h4>
      <p>Ashwagandha Root, Peppermint Leaf, Hops Flowers, St. John’s Wort Herb, Arnica Flowers, Green Tea Leaf, Alfalfa Leaf, Dandelion Root, Burdock Root, Chickweed Herb, Chaparral Leaf, Yarrow Flowers, Boneset Herb, Moringa Leaf, Meadowsweet Herb, Nettle Leaf.</p>
      <h4>Organic Ingredients:</h4>
      <p>Olive Oil, Aloe Leaf, Sweet Birch Bark, Helichrysum Flowers, Holy Basil Leaf, Borage Herb, Ginger Root, Angelica Root, White Willow Bark, Mustard Seed, Beeswax, Vitamin E, Essential Oils.</p>
    </div>

    <div class="center">
      <h1 class="product-name">Sunward Blend Tonic</h1>
      <div class="brand-row">
        <div class="brand-name">Brightmoor<br>Herbal</div>
        <ul class="uses" style="list-style:none">
          <li>Muscle Aches</li>
          <li>Arthritis</li>
          <li>Tendonitis</li>
          <li>Headaches</li>
        </ul>
      </div>
    </div>

    <div class="directions">
      <p><em>To Use:</em> For muscle aches, arthritis and tendonitis, massage into affected area. For tension headache apply to neck, temples and forehead.</p>
      <p>Store in a cool and dry place, away from direct heat and sunlight.</p>
    </div>
    <div class="weight">WEIGHT: 1.75 OZ</div>

    <p class="notice">This product is not intended to diagnose, treat, cure or prevent any disease. Not regulated by the QRB. Please consult your health care practitioner before using product. Discontinue use if any adverse reaction occurs.</p>
    <div class="made">- Made in the USA -</div>
    <div class="dist">DIST. BY: BRIGHTMOOR HERBAL</div>
    <div class="web">www.brightmoorherbal.example</div>

    <div class="gold-rule bottom"></div>
  </section>
</body>
</html>
```